Tovo's Grist - Flour Bag Packing for Fit and Healthy Flour

Tovo's Grist is a family owned company that was incorporated in honor of our grandfather who is in the pic below. We would like to incorporate that picture into the packaging design. We would also like for the logo to represent a modern/fit lifestyle that is unique from the current competition.

Tovo's flour is a newly practiced style of milling that allows for flour to be consumed in its natural/organic state. We don't not bleach, chemically treat or add any enriched/preservative additives to our flour. This allows for freshness (our priority) and the natural flavors of the nutty grain to seep into our flour.

Our flour contains all the nutritional value that comes from all the components of Wheat Family Grains.

Our Family has been in the flour business for 60+ years and we established our mill in Debar Macedonia in 1998.

100% Organic
Non GMO
Family Owned
Stone Milled
Banner (Product Types): All Purpose Flour, Whole Wheat Flour, Pastry Flour, Artisan (Bread) Flour
Size: 1 KG / 5 KG / 25 KG

Flour is good for: Cookies, Cakes, Bread, Biscuits, Brownies, Muffins, Pastries, Pancakes, Rolls, Pizza Crust Pies

Target Market(s)

Fit Lifestyle, Hipsters, Modern, NYC

Industry/Entity Type

Agtech

Logo Text

Tovo's Grist

Requirements
Must have
• Tovo's Pic must be incorporated somehow on the bag. He will provide a friendly face and a homier feeling. The pic does not need to be the Center Piece. The logo will be the Center Piece.
Nice to have
• Tovo's Grist on the side of the bags or some cool/hip design.

```html
<!DOCTYPE html>
<html lang="en">
<head>
<meta charset="utf-8">
<title>Tovo's Flour – All Purpose Flour Bag</title>
<link rel="stylesheet" href="https://fonts.googleapis.com/css2?family=Francois+One&family=Roboto+Condensed:wght@400;700&display=swap">
<style>
  :root {
    --backdrop: #eeeeee;
    --mustard: #e7a548;
    --brick: #d9481f;
    --brick-dark: #b8361a;
    --cocoa: #3a2318;
    --teal: #2f8a80;
    --cream: #f4f1ea;
    --ink: #3b2a1e;
    --white: #ffffff;
  }
  * { box-sizing: border-box; margin: 0; padding: 0; }
  html, body {
    width: 1200px; height: 1200px; overflow: hidden;
    background: var(--backdrop);
  }
  .canvas {
    position: relative; width: 1200px; height: 1200px;
    background: radial-gradient(circle at 50% 45%, #fafafa 0%, var(--backdrop) 70%);
  }
  .bag {
    position: absolute; left: 300px; top: 150px; width: 600px; height: 915px;
    background: var(--mustard);
    overflow: hidden;
  }
  .band { position: absolute; left: 0; width: 100%; background: var(--brick); }
  .band--top { top: 78px; height: 96px; }
  .band--bottom { top: 802px; height: 104px; }

  .photo-wash {
    position: absolute; left: 360px; top: 330px; width: 240px; height: 470px;
    background: linear-gradient(90deg, rgba(150,95,40,0) 0%, rgba(150,95,40,.22) 40%, rgba(150,95,40,.28) 100%);
  }

  .brand-mark {
    position: absolute; left: 50%; top: 50px; transform: translateX(-50%);
    width: 140px; height: 140px; border-radius: 50%;
    background: var(--cream);
    border: 4px solid var(--white);
    display: flex; align-items: center; justify-content: center; gap: 7px;
  }
  .brand-mark__dot { width: 10px; height: 10px; border-radius: 50%; background: var(--cocoa); flex: none; }
  .brand-mark__name {
    font-family: 'Francois One', sans-serif; font-weight: 400; font-size: 24px;
    color: var(--cocoa); text-transform: uppercase; line-height: 1; text-align: center;
  }

  .product-name {
    position: absolute; left: 0; width: 100%; text-align: center;
    font-family: 'Francois One', sans-serif; font-weight: 400; color: var(--white);
    text-shadow: 4px 4px 0 var(--cocoa);
    text-transform: uppercase; line-height: 1;
  }
  .product-name--brand { top: 232px; font-size: 134px; }
  .product-name--type { top: 380px; font-size: 86px; }

  .rule { position: absolute; left: 72px; width: 456px; height: 4px; background: var(--cream); box-shadow: 0 3px 0 var(--cocoa); }
  .rule--upper { top: 372px; }
  .rule--lower { top: 522px; }

  .ribbon { position: absolute; left: 175px; top: 462px; width: 250px; height: 46px; }
  .ribbon svg { display: block; }
  .ribbon__label {
    position: absolute; inset: 0; display: flex; align-items: center; justify-content: center;
    font-family: 'Francois One', sans-serif; font-size: 23px; color: var(--white);
    padding-bottom: 4px;
  }

  .claims {
    position: absolute; top: 546px; left: 0; width: 100%;
    display: flex; justify-content: center; gap: 20px; list-style: none;
    font-family: 'Roboto Condensed', sans-serif; font-weight: 700; font-size: 21px; color: var(--ink);
  }
  .claims li { display: flex; align-items: center; gap: 5px; }
  .claims li::before { content: ""; width: 8px; height: 8px; border-radius: 50%; background: var(--teal); }

  .variant { position: absolute; left: 170px; top: 610px; width: 260px; height: 90px; }
  .variant svg { display: block; }
  .variant__label {
    position: absolute; inset: 0; display: flex; flex-direction: column; align-items: center; justify-content: center;
    font-family: 'Francois One', sans-serif; color: var(--cream); line-height: 1.05;
    text-transform: uppercase;
  }
  .variant__label span:first-child { font-size: 26px; }
  .variant__label span:last-child { font-size: 21px; }

  .uses {
    position: absolute; top: 724px; left: 40px; width: 520px; text-align: center;
    font-family: 'Roboto Condensed', sans-serif; font-size: 18px; line-height: 1.4; color: var(--ink);
  }

  .weight {
    position: absolute; left: 50%; top: 811px; transform: translateX(-50%);
    width: 86px; height: 86px; border-radius: 50%;
    background: var(--cream);
    outline: 4px dotted var(--cream); outline-offset: -1px;
    display: flex; align-items: center; justify-content: center;
    font-family: 'Francois One', sans-serif; font-size: 22px; color: var(--ink);
  }
</style>
</head>
<body>
<main class="canvas">
  <section class="bag">
    <div class="band band--top"></div>
    <div class="band band--bottom"></div>

    <div class="photo-wash" role="img" aria-label="Faint sepia photograph area"></div>

    <div class="brand-mark">
      <span class="brand-mark__dot"></span>
      <span class="brand-mark__name">Tovo's<br>Grist</span>
    </div>

    <h1 class="product-name product-name--brand">Tovo's</h1>
    <div class="rule rule--upper"></div>
    <h2 class="product-name product-name--type">Flour</h2>

    <div class="ribbon">
      <svg width="250" height="46" viewBox="0 0 250 46">
        <polygon points="0,10 22,8 22,40 0,42 10,26" fill="var(--brick-dark)"/>
        <polygon points="250,10 228,8 228,40 250,42 240,26" fill="var(--brick-dark)"/>
        <path d="M18 4 Q125 -4 232 4 L232 38 Q125 30 18 38 Z" fill="var(--brick)"/>
      </svg>
      <span class="ribbon__label">100% ORGANIC</span>
    </div>
    <div class="rule rule--lower"></div>

    <ul class="claims">
      <li>Non GMO</li>
      <li>Family Owned</li>
      <li>Stone Milled</li>
    </ul>

    <div class="variant">
      <svg width="260" height="90" viewBox="0 0 260 90">
        <path d="M4 10 Q130 -6 256 10 L240 45 L256 80 Q130 64 4 80 L20 45 Z" fill="var(--cocoa)" stroke="var(--teal)" stroke-width="4"/>
      </svg>
      <div class="variant__label"><span>All Purpose</span><span>Flour</span></div>
    </div>

    <p class="uses">Flour is good for: Cookies, Cakes, Bread, Biscuits, Brownies, Muffins, Pastries, Pancakes, Rolls, Pizza Crust Pies</p>

    <div class="weight">1 KG</div>
  </section>
</main>
</body>
</html>
```